Riverbend Trusted Home Care-Flyer for Patients

Our Home Health Care Agency, Riverbend Trusted Home Care, is seeking a flyer to advertise our services. We would like our flyer to convey professionalism, classiness and sophistication. We want our agency to come across as one that is well-established and recognized as being first-rate within the field.

We also want to appear original; we want to stand out.

Our theme colors, blue and green, from our logo should be incorporated into the flyer's design (refer below).

The top of the page should say (in a clear, bold font)-Seeking Care for your Loved One?

Our Logo, followed by our slogan, "Lean On Those Nearby", should be in the center. (This should make it appear as if our agency is the obvious solution to the consumer's quest in finding suitable care for their family member). This should be in a big font.
Below that, our agency's services should be listed in a very noticeable font...yet smaller than what's written above that.
The text should read:
Our Services Include:
*Experienced Certified Home Health Aides/ Live In Home Health Aides/Companions
*Nursing Services
*Alzheimer’s and Dementia Care
*Respite Care
*Postoperative Care
*Post Rehabilitation Care
*Running Errands
*Light Housekeeping
*Assistance with Bathing, Feeding and Grooming
*Meal Preparation
*Laundry and Linen Washing
*Mail and Bill Organization
*Medication Management
*Accompanying to Doctor’s Appointments
*And much more!
Below that, in a smaller, yet noticeable font:
As seasoned professionals, we know how to help our clients navigate and fulfill their various health care needs. Those nearby are here to help you get the attention that you merit.
Call Riverbend Trusted Home Care today to learn more about our first-rate services!
Below that, in a larger font, our phone number, website, our e-mail address.
*Out contact information will be provided to the project’s winner*.

*Pictures of Caregivers helping elderly patient should be included in the advertisement as well. *

We provided advertisements of other Home Health Care Agencies attached below to use as a reference. Once again, while we are aiming for a similar idea; however, our goal is to stand out as the community's premiere home health care agency, the one that they want to choose. We want to be original as well!

Size: Standard Computer Paper Size. 8.5” x 11”.

Feel free to utilize your creative, designer flair!
We look forward to seeing the results!
Good luck!

Industry/Entity Type

Home Health Care

Font styles to use
Sans Serif

Requirements
Must have
• Refer above.
Nice to have
• Refer to attachment below to see how other home health care agencies advertise. While we are aiming for a similar idea, we would like to incorporate our logo, slogan and colors to make this flyer more unique and stand out. We would like to appear original.

```html
<!DOCTYPE html>
<html lang="en">
<head>
<meta charset="utf-8">
<title>Riverbend Trusted Home Care – Patient Flyer</title>
<link rel="stylesheet" href="https://fonts.googleapis.com/css2?family=Montserrat:wght@300;400;600;800&display=swap">
<style>
  :root {
    --blue: #0f4c9b;
    --blue-deep: #0b3f86;
    --green: #7dc242;
    --white: #ffffff;
    --stage: #a9b5bc;
    --photo-light: #eef1f4;
    --photo-mid: #d9e1e6;
  }
  * { box-sizing: border-box; margin: 0; padding: 0; }
  html, body { width: 1200px; height: 1200px; overflow: hidden; }
  body {
    background: var(--stage);
    font-family: "Montserrat", Arial, sans-serif;
    position: relative;
  }
  .flyer {
    position: absolute;
    left: 160px; top: 30px;
    width: 880px; height: 1140px;
    overflow: hidden;
    background: var(--blue);
  }
  .flyer-shapes { position: absolute; inset: 0; }
  .headline {
    position: absolute; top: 48px; left: 0; width: 100%;
    text-align: center; color: var(--white);
  }
  .headline-lead { font-weight: 800; font-size: 40px; letter-spacing: 0.5px; }
  .headline-main { font-weight: 300; font-size: 80px; line-height: 1; margin-top: 2px; }

  .brand {
    position: absolute; left: 560px; top: 380px; width: 300px;
    text-align: center; color: var(--blue);
  }
  .brand-name {
    display: inline-flex; align-items: center; gap: 10px;
    font-weight: 600; font-size: 19px; color: var(--blue);
  }
  .brand-dot { width: 34px; height: 34px; border-radius: 50%; background: var(--green); flex: none; }
  .brand-slogan {
    margin-top: 26px; font-weight: 800; font-size: 36px; line-height: 1.05;
    text-transform: uppercase; color: var(--blue-deep);
  }

  .services-title {
    position: absolute; top: 712px; left: 0; width: 100%;
    display: flex; align-items: center; justify-content: center; gap: 18px;
    color: var(--white); font-weight: 800; font-size: 34px; text-transform: uppercase;
  }
  .services-title::before, .services-title::after {
    content: ""; width: 90px; height: 4px; background: var(--green);
  }
  .service-list {
    position: absolute; list-style: none; color: var(--white);
    font-size: 14px; font-weight: 400; line-height: 1.25;
  }
  .service-list li {
    position: relative; padding: 6px 0 6px 28px;
    border-bottom: 1px solid rgba(255,255,255,0.35);
  }
  .service-list li::before {
    content: ""; position: absolute; left: 0; top: 6px;
    width: 16px; height: 16px; border-radius: 50%; border: 2px solid var(--green);
  }
  .service-list li::after {
    content: ""; position: absolute; left: 5px; top: 9px;
    width: 5px; height: 8px; border: solid var(--green); border-width: 0 2px 2px 0;
    transform: rotate(45deg);
  }
  .col-one { left: 44px; top: 780px; width: 280px; }
  .col-two { left: 345px; top: 780px; width: 235px; }
  .col-three { left: 600px; top: 780px; width: 250px; }
  .more-pill {
    position: absolute; left: 600px; top: 992px;
    background: var(--white); color: var(--blue); border-radius: 14px;
    padding: 5px 16px 5px 30px; font-weight: 800; font-size: 13px; text-transform: uppercase;
  }
  .more-pill::before {
    content: ""; position: absolute; left: 12px; top: 6px;
    width: 5px; height: 9px; border: solid var(--green); border-width: 0 2px 2px 0;
    transform: rotate(45deg);
  }

  .contact {
    position: absolute; right: 36px; top: 1030px; text-align: left; color: var(--white);
  }
  .contact-phone {
    display: flex; align-items: center; gap: 10px;
    font-weight: 800; font-size: 34px;
  }
  .contact-line {
    display: flex; align-items: center; gap: 10px;
    font-size: 14px; font-weight: 600; margin-top: 4px; padding-left: 4px;
  }
  .contact svg { flex: none; }
  .about {
    position: absolute; left: 40px; top: 1068px; width: 420px;
    color: var(--blue-deep); font-size: 11px; line-height: 1.35; font-weight: 400;
  }
</style>
</head>
<body>
  <main class="flyer">
    <svg class="flyer-shapes" width="880" height="1140" viewBox="0 0 880 1140">
      <defs>
        <linearGradient id="photoTone" x1="0" y1="0" x2="1" y2="0">
          <stop offset="0" stop-color="var(--photo-mid)"/>
          <stop offset="0.35" stop-color="#c7d6da"/>
          <stop offset="0.6" stop-color="var(--photo-light)"/>
          <stop offset="1" stop-color="var(--photo-light)"/>
        </linearGradient>
      </defs>
      <rect x="0" y="150" width="880" height="620" fill="url(#photoTone)" role="img" aria-label="Photo of a smiling caregiver with her hands on the shoulders of a happy elderly man"/>
      <path d="M0 0 H880 V205 Q480 245 0 325 Z" fill="var(--green)"/>
      <path d="M0 0 H880 V192 Q480 230 0 308 Z" fill="var(--white)"/>
      <path d="M0 0 H880 V176 Q480 214 0 292 Z" fill="var(--blue)"/>
      <path d="M0 690 Q440 660 880 560 V1140 H0 Z" fill="var(--green)"/>
      <path d="M0 705 Q440 675 880 578 V1140 H0 Z" fill="var(--blue)"/>
      <path d="M0 998 L380 1028 L880 968 V1140 H0 Z" fill="var(--white)"/>
      <path d="M0 1010 L380 1042 L880 981 V1140 H0 Z" fill="var(--green)"/>
    </svg>

    <header class="headline">
      <p class="headline-lead">SEEKING CARE FOR YOUR</p>
      <h1 class="headline-main">LOVED ONE?</h1>
    </header>

    <section class="brand">
      <div class="brand-name"><span class="brand-dot"></span>Riverbend Trusted Home Care</div>
      <p class="brand-slogan">Lean On<br>Those<br>Nearby</p>
    </section>

    <h2 class="services-title">Our Services Include</h2>

    <ul class="service-list col-one">
      <li>Experienced Certified Home Health Aides/ Live In Home Health Aides/Companions</li>
      <li>Nursing Services</li>
      <li>Alzheimer’s and Dementia Care</li>
      <li>Respite Care</li>
      <li>Postoperative Care</li>
    </ul>
    <ul class="service-list col-two">
      <li>Post Rehabilitation Care</li>
      <li>Running Errands</li>
      <li>Light Housekeeping</li>
      <li>Assistance with Bathing, Feeding and Grooming</li>
      <li>Meal Preparation</li>
    </ul>
    <ul class="service-list col-three">
      <li>Laundry and Linen Washing</li>
      <li>Mail and Bill Organization</li>
      <li>Medication Management</li>
      <li>Accompanying to Doctor’s Appointments</li>
    </ul>
    <p class="more-pill">And much more!</p>

    <section class="contact">
      <p class="contact-phone">
        <svg width="26" height="26" viewBox="0 0 24 24" fill="none" stroke="#fff" stroke-width="2"><path d="M5 3h4l2 5-2.5 1.5a11 11 0 0 0 6 6L16 13l5 2v4a2 2 0 0 1-2 2A16 16 0 0 1 3 5a2 2 0 0 1 2-2z"/></svg>
        (555) 318-2046
      </p>
      <p class="contact-line">
        <svg width="14" height="14" viewBox="0 0 24 24" fill="none" stroke="#fff" stroke-width="2"><circle cx="12" cy="12" r="10"/><path d="M2 12h20M12 2a15 15 0 0 1 0 20M12 2a15 15 0 0 0 0 20"/></svg>
        www.riverbendtrustedcare.com
      </p>
      <p class="contact-line">
        <svg width="14" height="14" viewBox="0 0 24 24" fill="none" stroke="#fff" stroke-width="2"><rect x="2" y="5" width="20" height="14" rx="1"/><path d="M2 6l10 7 10-7"/></svg>
        hello@riverbendtrustedcare.com
      </p>
    </section>

    <p class="about">As seasoned professionals, we know how to help our clients navigate and fulfill their various health care needs. Those nearby are here to help you get the attention that you merit. Call Riverbend Trusted Home Care today to learn more about our first-rate services!</p>
  </main>
</body>
</html>
```